Corvento Franchise Services
Design business cards , stationery and banner
Creater,
The ai file is included in the zip folder.
Thanks for the design so far. Can you make sure you include business cards and stationery in your submissions. Thanks
sir plzz upload the logo in ai file

```html
<!DOCTYPE html>
<html lang="en">
<head>
<meta charset="utf-8">
<title>Corvento Franchise Services – Business Cards</title>
<link rel="stylesheet" href="https://fonts.googleapis.com/css2?family=Cinzel:wght@400;600;700&display=swap">
<style>
  :root {
    --blue: #1d62ae;
    --blue-deep: #0b3d7e;
    --blue-light: #3a8fd6;
    --green: #8fb52b;
    --green-light: #b9d44a;
    --green-deep: #5f8a1c;
    --ink: #2a2a2a;
    --grey: #6a6a6a;
    --card-border: #c9c9c9;
    --white: #ffffff;
  }
  * { margin: 0; padding: 0; box-sizing: border-box; }
  html, body { width: 1200px; height: 701px; overflow: hidden; background: var(--white); }
  body { position: relative; font-family: "Cinzel", serif; }

  .card {
    position: absolute;
    width: 516px;
    height: 314px;
    overflow: hidden;
    border: 1px solid var(--card-border);
  }
  .card--front { left: 72px; top: 28px; background: var(--white); }
  .card--back  { left: 612px; top: 28px; background: var(--white); }
  .card--green { left: 72px; top: 364px;
    background: radial-gradient(ellipse at 50% 50%, var(--green-light) 0%, var(--green) 55%, var(--green-deep) 100%); }
  .card--blue  { left: 612px; top: 364px;
    background: radial-gradient(ellipse at 50% 50%, var(--blue-light) 0%, var(--blue) 55%, var(--blue-deep) 100%); }

  .card__swoosh { position: absolute; inset: 0; width: 100%; height: 100%; }

  .wordmark { position: absolute; display: flex; align-items: center; gap: 10px; color: var(--ink); }
  .wordmark__dot { border-radius: 50%; background: var(--blue); flex: none; }
  .wordmark__text { font-weight: 700; letter-spacing: 1px; line-height: 1; }
  .wordmark__sub { display: block; font-weight: 700; letter-spacing: 2px; margin-top: 4px; }

  .card--front .wordmark { left: 22px; top: 32px; }
  .card--front .wordmark__dot { width: 44px; height: 44px; }
  .card--front .wordmark__text { font-size: 26px; }
  .card--front .wordmark__sub { font-size: 9px; }

  .card--back .wordmark { left: 50%; top: 50%; transform: translate(-50%, -50%); gap: 14px; }
  .card--back .wordmark__dot { width: 64px; height: 64px; }
  .card--back .wordmark__text { font-size: 38px; }
  .card--back .wordmark__sub { font-size: 12px; letter-spacing: 3px; }

  .contact {
    position: absolute; right: 18px; top: 136px;
    text-align: right; color: var(--white);
  }
  .contact__name { font-size: 22px; font-weight: 400; letter-spacing: 1px; }
  .contact__role { font-size: 12px; margin-top: 2px; letter-spacing: 0.5px; }
  .contact__details { margin-top: 22px; font-size: 11px; line-height: 19px; letter-spacing: 0.3px; }

  .emblem { position: absolute; left: 50%; top: 50%; width: 96px; height: 96px; transform: translate(-50%, -55%);
    border-radius: 50%; background: var(--blue); }
  .card--blue .emblem { background: var(--green); }
</style>
</head>
<body>

  <section class="card card--front">
    <svg class="card__swoosh" viewBox="0 0 516 314" preserveAspectRatio="none" aria-hidden="true">
      <defs>
        <linearGradient id="frontBlue" x1="0" y1="0" x2="1" y2="1">
          <stop offset="0" stop-color="#2c78c6"/>
          <stop offset="1" stop-color="#0b3d7e"/>
        </linearGradient>
      </defs>
      <path d="M0,184 C160,150 360,120 516,30 L516,314 L0,314 Z" fill="var(--green)"/>
      <path d="M0,196 C170,160 370,128 516,44 L516,314 L0,314 Z" fill="var(--white)"/>
      <path d="M0,202 C170,166 370,134 516,50 L516,314 L0,314 Z" fill="url(#frontBlue)"/>
    </svg>
    <div class="wordmark">
      <span class="wordmark__dot"></span>
      <span class="wordmark__text">CORVENTO<span class="wordmark__sub">FRANCHISE SERVICES</span></span>
    </div>
    <div class="contact">
      <p class="contact__name">Fiona Hartley</p>
      <p class="contact__role">Managing Director</p>
      <p class="contact__details">
        14B Carrick Road<br>
        Westmuir, Glasgow, G70 2QP<br>
        Phone: 01632 960418 | Cell: 07700900236 | Fax: 01632 960418<br>
        Email: fiona@corventofranchising.com<br>
        www.corventofranchising.com
      </p>
    </div>
  </section>

  <section class="card card--back">
    <div class="wordmark">
      <span class="wordmark__dot"></span>
      <span class="wordmark__text">CORVENTO<span class="wordmark__sub">FRANCHISE SERVICES</span></span>
    </div>
  </section>

  <section class="card card--green">
    <span class="emblem"></span>
  </section>

  <section class="card card--blue">
    <span class="emblem"></span>
  </section>

</body>
</html>
```